Bref créative
Stationery for bright harbor company
Stationery for my company
Professional
Farhan Tariq Baloch
General Manager
Prince Faisal Street,
Al Warood,
Riyadh,
Saudi Arabia.
P.O.Box:5831-6-40921-3158.
farhan@br1ghth4rb0r.example
www.br1ghth4rb0r.example
C.R.
I want something creative, plus if it is possible can you put the information editable so I can put the other names and titles for the other co - workers
My logo or something creative
logo to be used
like this

```html
<!DOCTYPE html>
<html lang="en">
<head>
<meta charset="utf-8">
<title>Bright Harbor Company – Stationery</title>
<link href="https://fonts.googleapis.com/css2?family=Open+Sans:wght@400;700&display=swap" rel="stylesheet">
<style>
:root{
  --backdrop:#6b4424;
  --paper:#ffffff;
  --navy:#0b2a4a;
  --blue:#1a73b8;
  --sky:#5fb0e4;
  --ink:#33404d;
  --muted:#8a949e;
  --faint:#e3e8ee;
  --label:#f3eadf;
}
*{box-sizing:border-box;margin:0;padding:0}
html,body{width:1200px;height:540px;overflow:hidden}
body{background:var(--backdrop);font-family:"Open Sans",Arial,sans-serif;color:var(--ink);position:relative}
.sheet,.envelope,.card{position:absolute;background:var(--paper);overflow:hidden;box-shadow:0 2px 6px rgba(0,0,0,.35)}
.swoosh{position:absolute;left:0;bottom:0;width:100%;display:block}
.brand{display:flex;align-items:center;gap:5px;position:absolute}
.brand-dot{width:16px;height:16px;border-radius:50%;background:var(--navy)}
.brand-name{font-weight:700;color:var(--navy);font-size:9px;letter-spacing:.3px;white-space:nowrap}
.sender{position:absolute;font-size:4.2px;line-height:6px;color:var(--muted);white-space:nowrap}
.sender strong{color:var(--ink);font-size:4.6px}
.mark-faint{position:absolute;display:flex;flex-direction:column;align-items:center;gap:10px}
.mark-faint .ring{border-radius:50%;background:var(--faint)}
.mark-faint .word{font-weight:700;color:var(--faint);white-space:nowrap}
.option-label{position:absolute;color:var(--label);font-size:17px;top:506px}

/* letterhead */
.letterhead{left:43px;top:24px;width:317px;height:468px}
.letterhead .brand{left:22px;top:22px}
.letterhead .sender{left:202px;top:18px}
.letterhead .mark-faint{left:48px;top:140px}
.letterhead .ring{width:200px;height:200px}
.letterhead .word{font-size:22px}

/* fax */
.fax{left:389px;top:24px;width:319px;height:468px}
.fax .brand{left:20px;top:22px}
.fax-title{position:absolute;left:20px;top:76px;font-size:15px;color:var(--ink)}
.fax-fields{position:absolute;left:20px;top:104px;width:280px;display:grid;grid-template-columns:1fr 1fr;column-gap:10px;row-gap:8px}
.fax-field{font-size:4.5px;color:var(--muted);border-bottom:.6px solid #9aa3ac;height:10px}
.fax-checks{position:absolute;left:20px;top:182px;display:flex;gap:12px;font-size:4.3px;color:var(--muted);white-space:nowrap}
.fax-checks span::before{content:"";display:inline-block;width:5px;height:5px;border:.6px solid #8a949e;margin-right:3px;vertical-align:-1px}
.fax .mark-faint{left:200px;top:320px;gap:6px}
.fax .ring{width:78px;height:78px}
.fax .word{font-size:8px}
.fax-footer{position:absolute;left:0;width:100%;bottom:30px;text-align:center;font-size:4px;color:var(--muted);white-space:nowrap}

/* envelopes */
.envelope-back{left:732px;top:108px;width:444px;height:118px}
.envelope-back .flap{position:absolute;left:0;top:0;width:100%;height:70px}
.envelope-back .brand{left:202px;top:6px}
.envelope-back .brand-dot{width:12px;height:12px;background:var(--paper);opacity:.8}
.envelope-back .brand-name{color:var(--paper);font-size:6px}
.envelope-front{left:768px;top:236px;width:408px;height:122px}
.envelope-front .brand{left:14px;top:10px}
.envelope-front .brand-name{font-size:7px}
.envelope-front .brand-dot{width:13px;height:13px}
.envelope-front .mark-faint{right:16px;top:36px}
.envelope-front .ring{width:36px;height:36px}

/* cards */
.card{top:408px;width:196px;height:84px}
.card-front{left:763px}
.card-front .brand{left:12px;top:32px}
.card-front .brand-name{font-size:9px}
.card-back{left:972px}
.card-back .sender{left:10px;top:10px}
.card-back .brand{right:10px;top:18px}
.card-back .brand-dot{width:22px;height:22px}
</style>
</head>
<body>

<svg width="0" height="0" style="position:absolute" aria-hidden="true">
  <defs>
    <linearGradient id="wave-navy" x1="0" x2="1"><stop offset="0" stop-color="#0b2a4a"/><stop offset="1" stop-color="#154b82"/></linearGradient>
    <linearGradient id="wave-blue" x1="0" x2="1"><stop offset="0" stop-color="#5fb0e4"/><stop offset="1" stop-color="#1a73b8"/></linearGradient>
    <symbol id="swoosh" viewBox="0 0 300 40" preserveAspectRatio="none">
      <path d="M0 22 C80 8 170 40 300 6 L300 40 L0 40Z" fill="url(#wave-blue)"/>
      <path d="M0 30 C90 18 180 44 300 16 L300 40 L0 40Z" fill="url(#wave-navy)"/>
      <path d="M0 36 C100 28 190 46 300 28 L300 40 L0 40Z" fill="#ffffff" opacity=".25"/>
    </symbol>
  </defs>
</svg>

<!-- Option 1: letterhead -->
<section class="sheet letterhead" aria-label="Letterhead">
  <div class="brand"><span class="brand-dot"></span><span class="brand-name">Brightharbor</span></div>
  <div class="sender">
    <strong>bright harbor company</strong><br>
    Office address line one<br>
    City, Country<br>
    Postal box line<br>
    Tel: 000 000 0000<br>
    Fax: 000 000 0000<br>
    www.br1ghth4rb0r.example
  </div>
  <div class="mark-faint"><span class="ring"></span><span class="word">Brightharbor</span></div>
  <svg class="swoosh" height="46"><use href="#swoosh"/></svg>
</section>
<p class="option-label" style="left:170px">Option 1</p>

<!-- Option 2: fax -->
<section class="sheet fax" aria-label="Fax cover sheet">
  <div class="brand"><span class="brand-dot"></span><span class="brand-name">Brightharbor</span></div>
  <h1 class="fax-title">FAX</h1>
  <div class="fax-fields">
    <div class="fax-field">To:</div><div class="fax-field">From:</div>
    <div class="fax-field">Fax:</div><div class="fax-field">Pages:</div>
    <div class="fax-field">Phone:</div><div class="fax-field">Date:</div>
    <div class="fax-field">Re:</div><div class="fax-field">CC:</div>
  </div>
  <div class="fax-checks">
    <span>Urgent</span><span>For Review</span><span>Please Comment</span><span>Please Reply</span><span>Please Recycle</span>
  </div>
  <div class="mark-faint"><span class="ring"></span><span class="word">Brightharbor</span></div>
  <p class="fax-footer">Office address line, City, Country · Tel: 000 000 0000 · www.br1ghth4rb0r.example</p>
  <svg class="swoosh" height="40"><use href="#swoosh"/></svg>
</section>
<p class="option-label" style="left:516px">Option 2</p>

<!-- Envelope back -->
<section class="envelope envelope-back" aria-label="Envelope back">
  <svg class="flap" viewBox="0 0 444 70" preserveAspectRatio="none">
    <path d="M0 0 H444 V22 L222 70 L0 22Z" fill="url(#wave-navy)"/>
    <path d="M0 22 L222 70 L444 22" fill="none" stroke="#5fb0e4" stroke-width="1.5"/>
  </svg>
  <div class="brand"><span class="brand-dot"></span><span class="brand-name">Brightharbor</span></div>
</section>

<!-- Envelope front -->
<section class="envelope envelope-front" aria-label="Envelope front">
  <div class="brand"><span class="brand-dot"></span><span class="brand-name">Brightharbor</span></div>
  <div class="mark-faint"><span class="ring"></span></div>
  <svg class="swoosh" height="18"><use href="#swoosh"/></svg>
</section>

<!-- Business cards -->
<section class="card card-front" aria-label="Business card front">
  <div class="brand"><span class="brand-dot"></span><span class="brand-name">Brightharbor</span></div>
  <svg class="swoosh" height="16"><use href="#swoosh"/></svg>
</section>
<section class="card card-back" aria-label="Business card back">
  <div class="sender">
    <strong>Staff Name</strong><br>
    Job Title<br>
    Office address line<br>
    City, Country<br>
    Tel: 000 000 0000<br>
    www.br1ghth4rb0r.example
  </div>
  <div class="brand"><span class="brand-dot"></span></div>
  <svg class="swoosh" height="16"><use href="#swoosh"/></svg>
</section>

</body>
</html>
```